Design some Stationery and Business Cards

I need help with stationary (letters and envelopes) layout and business card layouts. I would like something modern/clean with the typeface and some clean layouts. I've attached a few samples along the lines of what I was thinking, but please use your best judgement. Also, I've attached the logo - can you remove the "LLC" part in the final rendering? Also, please be patient with any back and forth to tweak the design layout.

As for the contact info here is information

Dorian P. Whitcombe, Esq.

438 Larch Avenue, Suite 7
Corwin Falls, MA 01942

P: 781-364-5172
C: 857-619-2038

```html
<!DOCTYPE html>
<html lang="en">
<head>
<meta charset="utf-8">
<title>Whitcombe Law Stationery</title>
<link href="https://fonts.googleapis.com/css2?family=Lato:wght@400;700&display=swap" rel="stylesheet">
<style>
  :root {
    --backdrop: #1b1a3d;
    --ink: #2b2872;
    --paper: #ffffff;
    --text: #2e2c5e;
  }
  * { margin: 0; padding: 0; box-sizing: border-box; }
  html, body { width: 1200px; height: 673px; overflow: hidden; }
  body {
    position: relative;
    background: var(--backdrop);
    font-family: "Lato", Arial, sans-serif;
    color: var(--text);
  }
  .sheet { position: absolute; background: var(--paper); overflow: hidden; }

  /* brand lockup */
  .brand { position: absolute; display: flex; flex-direction: column; align-items: center; }
  .brand-square { border: 2px solid var(--ink); }
  .brand-name {
    color: var(--ink); font-weight: 400; text-transform: uppercase;
    text-align: center; line-height: 1.05; letter-spacing: 0.02em; white-space: nowrap;
  }
  .brand-name span {
    display: block; font-size: 0.55em; letter-spacing: 0.12em;
    border-top: 1px solid var(--ink); margin-top: 2px; padding-top: 1px;
  }

  .contact { position: absolute; color: var(--text); }
  .contact p { white-space: nowrap; }
  .contact .line { display: flex; align-items: center; gap: 6px; }
  .contact svg { fill: var(--ink); flex: none; }

  /* letterhead */
  .letterhead { left: 28px; top: 27px; width: 477px; height: 617px; }
  .letterhead .footer-band { position: absolute; left: 0; bottom: 0; width: 100%; height: 12px; background: var(--ink); }
  .letterhead .brand { left: 38px; top: 40px; }
  .letterhead .brand-square { width: 36px; height: 46px; }
  .letterhead .brand-name { font-size: 15px; margin-top: 6px; }
  .letterhead .contact { left: 325px; top: 35px; font-size: 11px; }
  .letterhead .contact .address { line-height: 15px; margin-bottom: 9px; }
  .letterhead .contact .line { height: 15px; }

  /* business card */
  .card { left: 532px; top: 28px; width: 640px; height: 180px; }
  .card .divider { position: absolute; left: 318px; top: 0; width: 4px; height: 100%; background: var(--backdrop); }
  .card .card-brand { position: absolute; left: 22px; top: 22px; align-items: stretch; }
  .card .card-brand .brand-name { font-size: 20px; }
  .card .person { position: absolute; left: 22px; top: 64px; font-size: 12px; font-weight: 700; color: var(--ink); }
  .card .contact { left: 22px; top: 88px; font-size: 9px; }
  .card .contact .address { line-height: 12px; margin-bottom: 8px; }
  .card .contact .line { height: 12.5px; gap: 5px; }
  .card .feature-frame {
    position: absolute; left: 263px; top: 11px; width: 117px; height: 158px;
    border: 5px solid var(--ink);
  }
  .card .side-brand { left: 550px; top: 96px; }
  .card .side-brand .brand-square { width: 26px; height: 34px; }
  .card .side-brand .brand-name { font-size: 11px; margin-top: 4px; }

  /* envelope */
  .envelope { left: 532px; top: 240px; width: 640px; height: 404px; }
  .envelope .flap { position: absolute; left: 0; top: 0; width: 100%; height: 89px; background: var(--ink); border-radius: 48px 48px 0 0; }
  .envelope .flap-brand { left: 536px; top: 18px; transform: rotate(180deg); }
  .envelope .flap-brand .brand-square { width: 28px; height: 36px; border-color: var(--paper); }
  .envelope .flap-brand .brand-name { font-size: 11px; color: var(--paper); margin-top: 4px; }
  .envelope .flap-brand .brand-name span { border-top-color: var(--paper); }
  .envelope .main-brand { left: 48px; top: 123px; }
  .envelope .main-brand .brand-square { width: 44px; height: 58px; }
  .envelope .main-brand .brand-name { font-size: 22px; margin-top: 8px; }
  .envelope .contact { left: 48px; top: 245px; font-size: 14.5px; }
  .envelope .contact .address { line-height: 21px; margin-bottom: 12px; }
  .envelope .contact .line { height: 20px; gap: 8px; }
  .envelope .window { position: absolute; left: 304px; top: 249px; width: 283px; height: 104px; background: var(--ink); border-radius: 10px; }
</style>
</head>
<body>

<svg width="0" height="0" style="position:absolute">
  <defs>
    <symbol id="icon-phone" viewBox="0 0 24 24"><path d="M6.6 10.8c1.4 2.8 3.8 5.1 6.6 6.6l2.2-2.2c.3-.3.7-.4 1-.2 1.1.4 2.3.6 3.6.6.6 0 1 .4 1 1V20c0 .6-.4 1-1 1C10.6 21 3 13.4 3 4c0-.6.4-1 1-1h3.5c.6 0 1 .4 1 1 0 1.3.2 2.5.6 3.6.1.3 0 .7-.2 1L6.6 10.8z"/></symbol>
    <symbol id="icon-mobile" viewBox="0 0 24 24"><path d="M8 2h8a2 2 0 0 1 2 2v16a2 2 0 0 1-2 2H8a2 2 0 0 1-2-2V4a2 2 0 0 1 2-2zm0 3v13h8V5H8zm4 14.5a1 1 0 1 0 0 .01z"/></symbol>
    <symbol id="icon-pointer" viewBox="0 0 24 24"><path d="M5 3l14 8-6 1.5 3.5 7-2.5 1.2-3.4-7L6 18z"/></symbol>
  </defs>
</svg>

<!-- Letterhead -->
<section class="sheet letterhead">
  <div class="brand">
    <div class="brand-square"></div>
    <div class="brand-name">Whitcombe<span>Law</span></div>
  </div>
  <div class="contact">
    <p class="address">438 Larch Avenue, Suite 7<br>Corwin Falls, MA 01942</p>
    <p class="line"><svg width="9" height="9"><use href="#icon-phone"/></svg>781-364-5172</p>
    <p class="line"><svg width="9" height="9"><use href="#icon-mobile"/></svg>857-619-2038</p>
    <p class="line"><svg width="9" height="9"><use href="#icon-pointer"/></svg>Dorian@whitlaw.com</p>
  </div>
  <div class="footer-band"></div>
</section>

<!-- Business card, front and back -->
<section class="sheet card">
  <div class="brand card-brand">
    <div class="brand-name">Whitcombe<span>Law</span></div>
  </div>
  <p class="person">Dorian P. Whitcombe, Esq.</p>
  <div class="contact">
    <p class="address">438 Larch Avenue, Suite 7<br>Corwin Falls, MA 01942</p>
    <p class="line"><svg width="8" height="8"><use href="#icon-phone"/></svg>781-364-5172</p>
    <p class="line"><svg width="8" height="8"><use href="#icon-mobile"/></svg>857-619-2038</p>
    <p class="line"><svg width="8" height="8"><use href="#icon-pointer"/></svg>Dorian@whitlaw.com</p>
  </div>
  <div class="feature-frame"></div>
  <div class="divider"></div>
  <div class="brand side-brand">
    <div class="brand-square"></div>
    <div class="brand-name">Whitcombe<span>Law</span></div>
  </div>
</section>

<!-- Envelope -->
<section class="sheet envelope">
  <div class="flap"></div>
  <div class="brand flap-brand">
    <div class="brand-square"></div>
    <div class="brand-name">Whitcombe<span>Law</span></div>
  </div>
  <div class="brand main-brand">
    <div class="brand-square"></div>
    <div class="brand-name">Whitcombe<span>Law</span></div>
  </div>
  <div class="contact">
    <p class="address">438 Larch Avenue, Suite 7<br>Corwin Falls, MA 01942</p>
    <p class="line"><svg width="12" height="12"><use href="#icon-phone"/></svg>781-364-5172</p>
    <p class="line"><svg width="12" height="12"><use href="#icon-mobile"/></svg>857-619-2038</p>
    <p class="line"><svg width="12" height="12"><use href="#icon-pointer"/></svg>Dorian@whitlaw.com</p>
  </div>
  <div class="window"></div>
</section>

</body>
</html>
```